Geschäftspapiere für Rechtsanwaltskanzlei
Zielgruppe
Rechtsanwaltskanzlei
Aufgabenstellung
Bitte inklusive Logo (sollte Recht, Digital/Apps, Medizin illustrieren) - habe das Preisgeld vor diesem Hintergrund erhöht.
Die Kanzlei arbeitet an der Schnittstelle von (Medizin-)Recht und Digital. Von daher wären wären Symbole/Gestaltung aus Bereich Medizin, Recht und Digital (z.B. Apps etc.) passend.
Das Briefpapier soll alle wichtigen Infos enthalten, aber dabei sehr klar gehalten werden und nicht überladen sein. Mir ist ein schlichtes und ansprechendes Design wichtig. Es soll nicht verspielt sein.
Info auf Briefpapier:
Kanzlei für Medizinrecht
Rechtsanwalt Dr. Tilman Brecke - Fachanwalt für Medizinrecht
Bitte Platzhalter/Freitextfelder für die anderen anderen Angaben, wie:
- Adresse
- Telefon-Nr.
- Homepage
- E-Mail
- Bankdaten.

```html
<!DOCTYPE html>
<html lang="de">
<head>
<meta charset="utf-8">
<title>Briefpapier – Dr. Tilman Brecke Rechtsanwälte</title>
<link rel="stylesheet" href="https://fonts.googleapis.com/css2?family=Inter:wght@400;500;600&display=swap">
<style>
  :root {
    --stage: #353535;
    --paper: #ffffff;
    --accent: #3596b5;
    --ink: #5f5f5f;
    --ink-soft: #6e6e6e;
    --rule: #555555;
  }
  * { margin: 0; padding: 0; box-sizing: border-box; }
  html, body { width: 1200px; height: 840px; overflow: hidden; background: var(--stage); }
  body { font-family: "Inter", Arial, sans-serif; color: var(--ink); }

  .letterhead {
    position: absolute; left: 298px; top: 71px;
    width: 504px; height: 713px;
    background: var(--paper);
  }
  .top-band {
    position: absolute; left: 126px; top: 0;
    width: 252px; height: 8px; background: var(--accent);
  }

  .brand {
    position: absolute; left: 126px; top: 26px; width: 252px; height: 72px;
  }
  .brand-mark {
    position: absolute; left: 0; top: 26px;
    width: 22px; height: 22px; background: var(--accent);
  }
  .brand-name {
    position: absolute; right: 0; top: 21px;
    font-size: 22px; line-height: 26px; font-weight: 500;
    color: var(--ink); white-space: nowrap;
  }
  .brand-firm {
    position: absolute; left: 111px; right: 0; top: 46px;
    display: flex; align-items: center; gap: 3px;
    font-size: 7.6px; line-height: 10px; font-weight: 600; letter-spacing: 1.3px;
    color: var(--accent); white-space: nowrap;
  }
  .brand-firm::after {
    content: ""; flex: 1; height: 0.7px; background: var(--ink-soft);
  }
  .brand-specialty {
    position: absolute; right: 0; top: 57px;
    font-size: 10px; line-height: 13px; color: var(--ink); white-space: nowrap;
  }

  .sender-line {
    position: absolute; left: 90px; top: 139px;
    font-size: 5.8px; color: var(--ink);
    padding-bottom: 1px; border-bottom: 0.6px solid var(--ink);
    white-space: nowrap;
  }
  .sender-line .dot { color: var(--accent); }

  .fold-mark {
    position: absolute; left: 9px; top: 485px;
    width: 10px; height: 0.8px; background: var(--rule);
  }

  .footer-block {
    position: absolute; font-size: 6.6px; line-height: 10.2px;
    color: var(--ink); white-space: nowrap;
  }
  .footer-block .label { color: var(--accent); }
  .footer-bank { left: 27px; top: 672px; }
  .footer-register { left: 160px; top: 672px; }
  .footer-contact { left: 381px; top: 620px; line-height: 11px; }
  .footer-contact .address { margin-bottom: 4px; }
  .footer-contact .label { display: inline-block; width: 20px; }

  .footer-divider {
    position: absolute; width: 0.8px; background: var(--rule);
  }
  .footer-divider.first { left: 148px; top: 671px; height: 29px; }
  .footer-divider.second { left: 372px; top: 618px; height: 82px; }

  .bottom-band {
    position: absolute; left: 0; bottom: 0;
    width: 100%; height: 8px; background: var(--accent);
  }
</style>
</head>
<body>
  <main class="letterhead">
    <div class="top-band"></div>

    <header class="brand">
      <span class="brand-mark"></span>
      <span class="brand-name">Dr. Tilman Brecke</span>
      <span class="brand-firm">RECHTSANWÄLTE</span>
      <span class="brand-specialty">Fachanwalt für Medizinrecht</span>
    </header>

    <p class="sender-line">Birkenfelder Straße, 22 <span class="dot">•</span> 16352 Lindenau &nbsp;<span class="dot">•</span> Haselgrund</p>

    <div class="fold-mark"></div>

    <footer>
      <div class="footer-block footer-bank">
        <div><span class="label">Bank:</span> Sparkasse Rheinauen</div>
        <div><span class="label">IBAN:</span> DE XX 52140XX 4700008351</div>
        <div><span class="label">BIC-Swift:</span> RHAUDEOOXXX</div>
      </div>
      <div class="footer-divider first"></div>
      <div class="footer-block footer-register">
        <div>Amtsgericht Talbrück</div>
        <div><span class="label">Handelsregister:</span> 0000782</div>
        <div><span class="label">USt.-ID-Nr.:</span> DE0007820000</div>
      </div>
      <div class="footer-divider second"></div>
      <div class="footer-block footer-contact">
        <div class="address">
          <div>Birkenfelder Straße, 22</div>
          <div>16352 Lindenau</div>
          <div>Haselgrund</div>
        </div>
        <div><span class="label">Tel.</span> +49&nbsp; 000 000 47 3820</div>
        <div><span class="label">Fax.</span> +49&nbsp; 000 000&nbsp; 47 3821</div>
        <div><span class="label">Mail.</span> info@xxxxxx-tb.de</div>
        <div><span class="label">Web.</span> www.xxxxxx-tb.de</div>
      </div>
    </footer>

    <div class="bottom-band"></div>
  </main>
</body>
</html>
```